Design iOS App UI/UX for RehabGauge.com

Design UI for home screen/dashboard for my iOS/Android APP RehabGauge.
See attached screen shots and User Experience description. Also go to www.RehabGauge.com and see the website description (yes, it is still under construction, its broken and incomplete).
You are designing screen #2 #5 #6A, #6B 2&5 are very similar and 6A&6B are very similar.
To understand what you are working on, the main 8 functions of the App are:
Screen: Description:
5, 6D, 6D Get Property Info
6A, 6B, 7 Get After Repaired Value
9, 10, 11 Build a Budget
14, 14A, 15 Calculate Cost of Money
18, 19 Estimate Closing Costs
13, 13B 13A Enter Holding Costs
16, 17 Predict Cost of Sale
1, 2 Let the Dashboard drive your decision
The design aesthetic we are seeking is like the Homvara.com App, and the Nestiq App.
-Open your iOS 7 mail and launch the "new message" icon and the email template is similar to what we are looking for in UI design:
-Open your iOS 7 calendar and see transitions as you click from day to week to month for the kind of UX design input we are seeking
-We don't want special coding, but off the shelf solutions. So we want you to know what can be built with available code.
Thanks,
Carl Brinsted
P.S. Please send description of your experience and links to your work.
Target Market(s)
Our Target User #1 is a house remodel guy, 50 yrs old, skilled blue collar with some college and hands on attitude.
Our Target User #2 is a Realtor who sells these houses for the remodel Fix and Flip guy.
Our Target User #3 is a Hard Money Lender who lends money to our Fix and Flip guy. He is a small business loaning 100k to 300k to our flip guys for each project. He is lending his money, or money he has personally guaranteed with local banks or friends and family.
Our Target User #4 is a landlord looking to evaluate a buy and fix and hold property. Very similar to the User #1, but he spends time managing rental property.
Industry/Entity Type
Construction
Requirements
Must have
- Easy to see, read, clean design.
The top of screen #2 should show the Profit more clearly and compare it to the "70% ARV" scenario.
the 3,6 9 months can be buttons or shown smaller somehow.
Nice to have
- Flat design. clean and lean. look at the work of Lars Mendoza if you want to get creative.
Should not have
- flashy splashy, music label like, fashion model like, hokey, cute, silly, kitchy, country, 3-D.

```html
<!DOCTYPE html>
<html lang="en">
<head>
<meta charset="utf-8">
<title>RehabGauge – Property Info Screens</title>
<link rel="stylesheet" href="https://fonts.googleapis.com/css2?family=Merriweather:ital,wght@0,300;0,700;1,300&family=Source+Sans+3:ital,wght@0,300;0,400;0,600;1,400&display=swap">
<style>
  :root {
    --canvas: #ffffff;
    --header-blue: #29abe2;
    --accent-blue: #1f74bd;
    --screen-gray: #e6e7e8;
    --card-white: #ffffff;
    --photo-gray: #f2f2f2;
    --ink: #2b2b2b;
    --ink-soft: #4a4a4a;
    --tab-icon: #bdbdbd;
    --tab-text: #7a7a7a;
    --divider: #d2d3d4;
    --status-ink: #1f2a33;
  }
  * { box-sizing: border-box; margin: 0; padding: 0; }
  html, body { width: 1200px; height: 1014px; overflow: hidden; background: var(--canvas); }
  .canvas { position: relative; width: 1200px; height: 1014px; }

  .phone {
    position: absolute; width: 522px; height: 931px;
    background: var(--screen-gray); overflow: hidden;
    font-family: "Source Sans 3", sans-serif; color: var(--ink);
  }
  .phone--serif { left: 41px; top: 31px; }
  .phone--sans { left: 621px; top: 38px; }

  .app-header { position: absolute; left: 0; top: 0; width: 100%; height: 110px; background: var(--header-blue); }
  .status-bar { position: absolute; top: 11px; left: 6px; right: 6px; font-size: 16px; color: var(--status-ink); }
  .status-network { position: absolute; left: 0; }
  .status-time { position: absolute; left: 227px; }
  .nav-back { position: absolute; left: 16px; top: 56px; font-size: 27px; font-weight: 300; color: #e8f6fd; }
  .nav-title { position: absolute; left: 157px; top: 57px; font-size: 25px; font-weight: 700; color: #fff; }

  .card { position: absolute; left: 8px; width: 507px; background: var(--card-white); box-shadow: 0 1px 3px rgba(0,0,0,.18); }
  .photo-card { top: 116px; height: 324px; }
  .photo-area { position: absolute; left: 21px; top: 15px; width: 464px; height: 294px; background: var(--photo-gray); }
  .photo-caption { position: absolute; right: 19px; top: 440px; font-size: 16px; font-style: italic; color: var(--ink-soft); }

  .address-card { top: 494px; height: 85px; padding: 23px 0 0 41px; }
  .address-label { font-size: 20px; color: var(--accent-blue); line-height: 1.2; }
  .address-value { font-size: 20px; color: var(--ink); line-height: 1.25; }

  .stats-card { top: 593px; height: 248px; }
  .stat-row { position: absolute; left: 0; width: 100%; height: 40px; }
  .stat-value { position: absolute; right: 416px; top: 0; font-size: 36px; font-weight: 300; color: var(--accent-blue); line-height: 40px; }
  .stat-label { position: absolute; left: 121px; top: 8px; font-size: 20px; color: var(--ink-soft); line-height: 26px; }

  .tab-bar { position: absolute; left: 6px; right: 6px; top: 859px; bottom: 0; border-top: 2px solid var(--divider); }
  .tab { position: absolute; top: 11px; width: 110px; margin-left: -55px; text-align: center; }
  .tab-icon { display: block; margin: 0 auto; width: 32px; height: 32px; border-radius: 50%; background: var(--tab-icon); }
  .tab-label { display: block; margin-top: 6px; font-size: 13px; color: var(--tab-text); }

  /* serif variant */
  .phone--serif .status-bar { font-weight: 600; }
  .phone--serif .nav-back { font-family: "Source Sans 3", sans-serif; }
  .phone--serif .nav-title { font-family: "Merriweather", serif; font-size: 23px; }
  .phone--serif .photo-caption,
  .phone--serif .address-value,
  .phone--serif .stat-label,
  .phone--serif .tab-label { font-family: "Merriweather", serif; font-weight: 300; }
  .phone--serif .address-label { font-family: "Source Sans 3", sans-serif; font-weight: 400; }
  .phone--serif .address-value { font-size: 18px; }
  .phone--serif .stat-label { font-size: 18px; }
  .phone--serif .photo-caption { font-size: 15px; }
  .phone--serif .tab-label { font-size: 12px; }

  /* sans variant */
  .phone--sans .nav-title { font-weight: 700; }
  .phone--sans .address-label { font-weight: 600; }
</style>
</head>
<body>
<div class="canvas">

  <section class="phone phone--serif" aria-label="Property info screen, serif type option">
    <header class="app-header">
      <div class="status-bar"><span class="status-network">Network ●●●●●</span><span class="status-time">08:51 AM</span></div>
      <span class="nav-back">Back</span>
      <h1 class="nav-title">4418 Marlow Ct</h1>
    </header>
    <div class="card photo-card"><div class="photo-area" role="img" aria-label="Street view photo of the property"></div></div>
    <p class="photo-caption">images pulled from atlasview maps.</p>
    <div class="card address-card">
      <p class="address-label">Address</p>
      <p class="address-value">Street Name, City, ZIP code</p>
    </div>
    <div class="card stats-card">
      <div class="stat-row" style="top:26px"><span class="stat-value">1943</span><span class="stat-label">Square Feet</span></div>
      <div class="stat-row" style="top:78px"><span class="stat-value">3</span><span class="stat-label">Bedrooms</span></div>
      <div class="stat-row" style="top:129px"><span class="stat-value">2</span><span class="stat-label">Bathrooms</span></div>
      <div class="stat-row" style="top:181px"><span class="stat-value">1</span><span class="stat-label">Garrages</span></div>
    </div>
    <nav class="tab-bar">
      <div class="tab" style="left:45px"><span class="tab-icon"></span><span class="tab-label">Investments</span></div>
      <div class="tab" style="left:259px"><span class="tab-icon"></span><span class="tab-label">Suppliers</span></div>
      <div class="tab" style="left:474px"><span class="tab-icon"></span><span class="tab-label">About</span></div>
    </nav>
  </section>

  <section class="phone phone--sans" aria-label="Property info screen, sans type option">
    <header class="app-header">
      <div class="status-bar"><span class="status-network">Network &nbsp;●●●●●</span><span class="status-time">08:51 AM</span></div>
      <span class="nav-back">Back</span>
      <h1 class="nav-title">4418 Marlow Ct</h1>
    </header>
    <div class="card photo-card"><div class="photo-area" role="img" aria-label="Street view photo of the property"></div></div>
    <p class="photo-caption">images pulled from atlasview maps.</p>
    <div class="card address-card">
      <p class="address-label">Address</p>
      <p class="address-value">Street Name, City, ZIP code</p>
    </div>
    <div class="card stats-card">
      <div class="stat-row" style="top:26px"><span class="stat-value">1943</span><span class="stat-label">Square Feet</span></div>
      <div class="stat-row" style="top:78px"><span class="stat-value">3</span><span class="stat-label">Bedrooms</span></div>
      <div class="stat-row" style="top:129px"><span class="stat-value">2</span><span class="stat-label">Bathrooms</span></div>
      <div class="stat-row" style="top:181px"><span class="stat-value">1</span><span class="stat-label">Garrages</span></div>
    </div>
    <nav class="tab-bar">
      <div class="tab" style="left:45px"><span class="tab-icon"></span><span class="tab-label">Investments</span></div>
      <div class="tab" style="left:259px"><span class="tab-icon"></span><span class="tab-label">Suppliers</span></div>
      <div class="tab" style="left:474px"><span class="tab-icon"></span><span class="tab-label">About</span></div>
    </nav>
  </section>

</div>
</body>
</html>
```